Corporate Design für Rechtsanwalt (Arbeitsrecht und Gesellschaftsrecht)
Zielgruppe
Rechtsanwalt (Arbeitsrecht und Gesellschaftsrecht)
Aufgabenstellung
Benötigt wird ein schlichtes und modernes Corporate Design für einen Anwalt, der sich vorwiegend mit Arbeitsrecht (Arbeitnehmer wie Arbeitgeber) und Gesellschaftsrecht befasst. Das Logo soll Professionalität und Seriosität vermitteln. Ein Paragraphenzeichen oder eine Waage sollen bitte nicht enthalten sein, da dies „alle“ Rechtsanwälte haben. Die Rechtsgebiete Arbeitsrecht und Gesellschaftsrecht sollen nicht im Logo enthalten sein.
Folgender Inhalt muss untergebracht werden:
Tobias Renz
Rechtsanwalt
Auf dem Briefkopf müssen Bankverbindung, St.-Nr., USt-ID, Internetadresse und Kontaktdaten (Adresse, Telefon, Fax und Mailadresse) untergebracht werden. Diese Daten müssen selbstständig abänderbar sein.
Notwendig sind: Logo, Briefkopf und Visitenkarte.

```html
<!DOCTYPE html>
<html lang="de">
<head>
<meta charset="utf-8">
<title>Kanzlei Renz – Corporate Design</title>
<link rel="stylesheet" href="https://fonts.googleapis.com/css2?family=Montserrat:wght@600&family=Poppins:wght@400;500&family=Tinos&display=swap">
<style>
  :root {
    --blue: #1b64b0;
    --grey: #666666;
    --stage: #e4e3e4;
    --paper: #ffffff;
    --ink: #1c1c1c;
    --window: #e5e5e7;
  }
  * { box-sizing: border-box; margin: 0; padding: 0; }
  html, body { width: 1200px; height: 1200px; overflow: hidden; background: var(--paper); }
  .canvas { position: relative; width: 1200px; height: 1200px; font-family: "Poppins", sans-serif; color: var(--ink); }

  .hero { position: absolute; left: 0; top: 0; width: 1200px; height: 461px; background: var(--paper); }
  .stage { position: absolute; left: 0; top: 461px; width: 1200px; height: 739px; background: var(--stage); }

  /* Logo lockup: square + name only */
  .logo { position: absolute; display: flex; align-items: center; gap: 0.3em; font-family: "Montserrat", sans-serif; color: var(--blue); white-space: nowrap; line-height: 1; }
  .logo__square { width: 1.05em; height: 1.05em; background: var(--blue); flex: none; }
  .logo__name { font-size: 1em; font-weight: 600; letter-spacing: 0.02em; }
  .logo--white { color: #fff; }
  .logo--white .logo__square { background: #fff; }

  .logo--hero { left: 0; right: 0; justify-content: center; top: 200px; font-size: 60px; }

  /* Paper items */
  .sheet { position: absolute; background: var(--paper); box-shadow: 0 6px 10px rgba(0,0,0,0.22); overflow: hidden; }
  .band-top { position: absolute; left: 0; right: 0; top: 0; background: var(--blue); }
  .band-bottom { position: absolute; left: 0; right: 0; bottom: 0; background: var(--grey); }

  /* Letterhead */
  .letterhead { left: 94px; top: 498px; width: 476px; height: 664px; }
  .letterhead .band-top { height: 16px; }
  .letterhead .band-bottom { height: 15px; }
  .letterhead .logo { left: 0; right: 0; justify-content: center; top: 46px; font-size: 22px; }
  .letter-body { position: absolute; left: 46px; top: 124px; width: 386px; text-align: center; font-size: 9.4px; line-height: 15.6px; letter-spacing: 0.09em; }
  .signature { position: absolute; left: 290px; top: 494px; width: 86px; height: 52px; background: linear-gradient(135deg, #eef1f6, #dfe5ee); border-radius: 4px; }
  .letter-contact { position: absolute; left: 44px; top: 566px; font-size: 9px; line-height: 14px; font-style: normal; }
  .letter-finance { position: absolute; left: 236px; top: 566px; font-size: 9px; line-height: 14px; }

  /* Envelopes */
  .envelope { left: 624px; top: 501px; width: 482px; height: 221px; }
  .envelope .band-top { height: 13px; }
  .envelope .band-bottom { height: 13px; }
  .envelope .logo { left: 24px; top: 42px; font-size: 15px; }
  .envelope__window { position: absolute; left: 24px; top: 80px; width: 155px; height: 61px; background: var(--window); border-radius: 6px; }
  .contact-small { position: absolute; font-size: 5.6px; line-height: 9.8px; font-weight: 500; font-style: normal; }
  .envelope .contact-small { left: 24px; top: 150px; }

  .envelope-back { left: 622px; top: 736px; width: 484px; height: 230px; }
  .envelope-back .flap { position: absolute; left: 0; top: 0; }
  .envelope-back .band-bottom { height: 12px; }
  .envelope-back .logo--flipped { left: 0; right: 0; justify-content: center; top: 31px; font-size: 15px; transform: rotate(180deg); }
  .envelope-back .logo--front { left: 30px; top: 96px; font-size: 15px; }
  .envelope-back .contact-small { left: 30px; top: 159px; }

  /* Business cards */
  .card { position: absolute; top: 1030px; width: 231px; height: 132px; box-shadow: 0 6px 10px rgba(0,0,0,0.22); overflow: hidden; }
  .card--front { left: 617px; background: var(--blue); }
  .card--front .logo { left: 0; right: 0; justify-content: center; top: 58px; font-size: 13px; }
  .card--back { left: 875px; background: var(--paper); }
  .card--back .band-top { height: 7px; }
  .card--back .band-bottom { height: 7px; }
  .card--back .logo { left: 0; right: 0; justify-content: center; top: 20px; font-size: 11px; }
  .card__person { position: absolute; left: 8px; top: 76px; width: 162px; text-align: center; color: var(--blue); font-family: "Tinos", serif; }
  .card__name { font-size: 14px; letter-spacing: 0.01em; line-height: 1; text-transform: uppercase; }
  .card__role { font-size: 5.6px; letter-spacing: 0.42em; color: var(--grey); margin-top: 3px; }
  .card--back .contact-small { left: 143px; top: 66px; font-size: 5.2px; line-height: 10.2px; }
</style>
</head>
<body>
<main class="canvas">

  <section class="hero">
    <div class="logo logo--hero">
      <span class="logo__square"></span>
      <span class="logo__name">KANZLEI RENZ</span>
    </div>
  </section>

  <section class="stage"></section>

  <!-- Letterhead -->
  <article class="sheet letterhead">
    <div class="band-top"></div>
    <div class="logo">
      <span class="logo__square"></span>
      <span class="logo__name">KANZLEI RENZ</span>
    </div>
    <div class="letter-body">
      <p>Lorem ipsum dolor sit amet, consectetuer adipiscing elit, sed diam nonummy nibh euismod tincidunt ut laoreet dolore magna aliquam erat volutpat. Ut wisi enim ad minim veniam, quis nostrud exerci tation ullamcorper suscipit lobortis nisl ut aliquip ex ea commodo consequat. Duis autem vel eum iriure dolor in hendrerit in vulputate velit esse molestie consequat, vel illum dolore eu feugiat nulla facilisis at vero eros et accumsan et iusto odio dignissim qui blandit praesent luptatum zzril delenit augue duis dolore te feugait nulla facilisi.</p>
      <p>Lorem ipsum dolor sit amet, cons ectetuer adipiscing elit, sed diam nonummy nibh euismod tincidunt ut laoreet dolore magna aliquam erat volutpat. Ut wisi enim ad minim veniam, quis nostrud exerci tation ullamcorper suscipit lobortis nisl ut aliquip ex ea commodo consequat.</p>
      <p>Lorem ipsum dolor sit amet, consectetuer adipiscing elit, sed diam nonummy nibh euismod tincidunt ut laoreet dolore magna aliquam erat volutpat. Ut wisi enim ad minim veniam, quis nostrud exerci tation ullamcorper suscipit lobortis nisl ut aliquip ex ea commodo consequat. Duis autem vel eum iriure dolor in hendrerit in vulputate velit esse molestie consequat, vel illum dolore eu feugiat nulla facilisis at vero eros et accumsan et iusto odio dignissim qui blandit praesent luptatum zzril delenit augue duis dolore te feugait nulla facilisi.</p>
    </div>
    <div class="signature" role="img" aria-label="Handschriftliche Unterschrift"></div>
    <address class="letter-contact">
      Lindenweg 14, Bonn<br>
      T | 0228 410 552<br>
      F | 0228 410 553<br>
      info@kanzlei-renz.example<br>
      www.kanzlei-renz.example
    </address>
    <div class="letter-finance">
      Bank: Musterbank Bonn<br>
      IBAN DE12 3705 0198 0000 4105 52<br>
      BIC MUBADE33XXX<br>
      St.-Nr. 205/5712/0831<br>
      USt-ID DE 312 845 907
    </div>
    <div class="band-bottom"></div>
  </article>

  <!-- Envelope front -->
  <article class="sheet envelope">
    <div class="band-top"></div>
    <div class="logo">
      <span class="logo__square"></span>
      <span class="logo__name">KANZLEI RENZ</span>
    </div>
    <div class="envelope__window"></div>
    <address class="contact-small">
      Lindenweg 14, Bonn<br>
      T | 0228 410 552<br>
      F | 0228 410 553<br>
      info@kanzlei-renz.example<br>
      www.kanzlei-renz.example
    </address>
    <div class="band-bottom"></div>
  </article>

  <!-- Envelope back with flap -->
  <article class="sheet envelope-back">
    <svg class="flap" width="484" height="80" viewBox="0 0 484 80" aria-hidden="true">
      <path d="M0 0 H484 V2 Q484 80 404 80 H80 Q0 80 0 2 Z" fill="var(--blue)"/>
    </svg>
    <div class="logo logo--white logo--flipped">
      <span class="logo__square"></span>
      <span class="logo__name">KANZLEI RENZ</span>
    </div>
    <div class="logo logo--front">
      <span class="logo__square"></span>
      <span class="logo__name">KANZLEI RENZ</span>
    </div>
    <address class="contact-small">
      Lindenweg 14, Bonn<br>
      T | 0228 410 552<br>
      F | 0228 410 553<br>
      info@kanzlei-renz.example<br>
      www.kanzlei-renz.example
    </address>
    <div class="band-bottom"></div>
  </article>

  <!-- Business card front -->
  <article class="card card--front">
    <div class="logo logo--white">
      <span class="logo__square"></span>
      <span class="logo__name">KANZLEI RENZ</span>
    </div>
  </article>

  <!-- Business card back -->
  <article class="card card--back">
    <div class="band-top"></div>
    <div class="logo">
      <span class="logo__square"></span>
      <span class="logo__name">KANZLEI RENZ</span>
    </div>
    <div class="card__person">
      <div class="card__name">Tobias Renz</div>
      <div class="card__role">RECHTSANWALT</div>
    </div>
    <address class="contact-small">
      Lindenweg 14, Bonn<br>
      T | 0228 410 552<br>
      F | 0228 410 553<br>
      info@kanzlei-renz.example<br>
      www.kanzlei-renz.example
    </address>
    <div class="band-bottom"></div>
  </article>

</main>
</body>
</html>
```